PSD website for property company

Please read the brief thoroughly.

We are looking for a new website for a property group that does property acquisitions, property development and property management.
They buy, build and lease core inner city industrial assets in Sydney, Australia.
They also invest in residential developments.

Site menu
- Home page
- Property – sub menus include – Leasing ; Projects ; Investments ; Property Management
- Capital and finance
- About
- Contact

They like this website
https://www.vemlor.com.au/

They want the site to be clean, modern and bold.
They like few colors, even black and white is OK to submit

They have a logo and style guide and useable images here:
http://www.kruft.net/temp/PelworWeb2019.zip
The zip file is also attached to this project.
We have supplied some images to give you an idea, but we will also require you to provide at least 3 extra images from stock photos.
Use your imagination.

I am expecting a lot of similar designs, so be aware the photos you choose will be really important.
They want really 3 good stock photos used and supplied without charge.
Please not too generic, I repeat the quality of the photos is important.
You may provide several photos (but not in multiple submissions please) and we will choose the best three to be provided.

The winner will be selected on a single home page design and required to provide;
All photos use in original format without charge
A second ‘standard page’ template design based on the winning home page design

```html
<!DOCTYPE html>
<html lang="en">
<head>
<meta charset="utf-8">
<title>Pelwor — Standard Page</title>
<link href="https://fonts.googleapis.com/css2?family=Arimo:wght@400;700&display=swap" rel="stylesheet">
<style>
  :root{
    --ink:#2b2b2b;
    --text:#3a3a3a;
    --header:#3b3b3b;
    --bar:#2f2f2f;
    --white:#ffffff;
    --footer-bg:#f3f7ee;
    --sage:#8fae8a;
    --sky:#3f8fae;
    --facade:#2c3640;
    --muted:#555;
  }
  *{box-sizing:border-box;margin:0;padding:0}
  html,body{width:1200px;height:2643px;overflow:hidden}
  body{font-family:"Arimo",Helvetica,Arial,sans-serif;color:var(--text);background:var(--white);position:relative}

  .site-header{position:absolute;top:0;left:0;width:1200px;height:92px;background:var(--header);color:var(--white)}
  .nav-link{position:absolute;top:40px;font-size:10.5px;font-weight:700;letter-spacing:1.6px;text-transform:uppercase}
  .nav-link.property{left:37px}
  .nav-link.property::after{content:"";display:inline-block;margin-left:7px;border:4px solid transparent;border-top:4px solid var(--white);border-bottom:0;vertical-align:2px}
  .nav-link.capital{left:170px}
  .nav-link.about{left:1013px}
  .nav-link.contact{left:1105px}
  .brand{position:absolute;top:26px;left:0;width:1200px;text-align:center;font-size:37px;font-weight:700;letter-spacing:9px;line-height:40px;padding-left:9px}

  .hero{position:absolute;top:92px;left:0;width:1200px;height:292px;
    background:linear-gradient(100deg,#1d242c 0%,#2e3a45 35%,#34404b 50%,var(--sky) 58%,#4f9ebd 75%,#3a4650 100%)}
  .hero-title{position:absolute;left:39px;top:186px;font-size:40px;font-weight:700;color:var(--white)}

  .h2{font-size:24.5px;font-weight:700;color:var(--ink);line-height:30px}
  .intro-heading{position:absolute;left:39px;top:467px}
  .intro{position:absolute;left:39px;top:537px;width:830px;font-size:17.6px;line-height:26.7px;color:var(--text)}

  .col{position:absolute;top:702px;width:548px}
  .col.left{left:39px}
  .col.right{left:614px;top:702px}
  .col p{font-size:13.8px;line-height:20px;margin-bottom:20px}
  .col p.tight{margin-bottom:0}
  .col .h2{margin:42px 0 47px}
  .col.right .h2{margin:0 0 47px}

  .photo{display:block;width:545px;height:364px;margin-top:32px}
  .photo.glass{background:linear-gradient(160deg,#e6ebee 0%,#b9c2c8 45%,#d4d9dc 70%,#5d7a55 100%);height:365px;margin-top:40px}
  .photo.building{background:linear-gradient(120deg,#1a4a86 0%,#2e6aa8 35%,#8b8f93 60%,#3b2a2e 100%)}
  .caption{text-align:right;font-size:11.5px;font-style:italic;margin:18px 0 48px;color:var(--muted)}

  .to-top{position:absolute;left:1004px;top:2384px;width:54px;height:54px;background:var(--sage);z-index:2}
  .site-footer{position:absolute;top:2415px;left:0;width:1200px;height:164px;background:var(--footer-bg)}
  .footer-nav{position:absolute;top:56px;left:0;width:1200px;text-align:center;font-size:12.5px;color:var(--ink)}
  .footer-nav span{margin:0 13px}
  .social{position:absolute;top:100px;left:0;width:1200px;display:flex;justify-content:center;gap:18px}
  .social i{display:block;width:16px;height:16px;border-radius:50%;background:var(--ink)}
  .base-bar{position:absolute;top:2579px;left:0;width:1200px;height:64px;background:var(--bar);color:var(--white);font-size:10.5px}
  .base-bar .copy{position:absolute;left:37px;top:28px}
  .base-bar .contact{position:absolute;right:38px;top:28px;font-weight:700;letter-spacing:.3px}
</style>
</head>
<body>
<header class="site-header">
  <span class="nav-link property">Property</span>
  <span class="nav-link capital">Capital &amp; Finance</span>
  <div class="brand">PELWOR</div>
  <span class="nav-link about">About</span>
  <span class="nav-link contact">Contact</span>
</header>

<section class="hero" role="img" aria-label="Upward view of dark office towers against a blue sky">
  <h1 class="hero-title">Page Title</h1>
</section>

<h2 class="h2 intro-heading">Heading</h2>
<p class="intro">Optional Intro Text - Lorem ipsum dolor sit amet, consectetur adipiscing elit, sed do eiusmod tempor incididunt ut labore et dolore magna aliqua. Ut enim ad minim veniam, quis nostrud exercitation ullamco laboris nisi ut aliquip ex ea commodo consequat. Duis aute irure dolor in reprehenderit in voluptate velit esse cillum dolore eu fugiat nulla pariatur. Excepteur sint occaecat cupidatat non proident, sunt in culpa qui officia deserunt mollit anim id est laborum.</p>

<div class="col left">
  <p>Standard Body Text - Lorem ipsum dolor sit amet, consectetur adipiscing elit, sed do eiusmod tempor incididunt ut labore et dolore magna aliqua. Ut enim ad minim veniam, quis nostrud exercitation ullamco laboris nisi ut aliquip ex ea commodo consequat. Duis aute irure dolor in reprehenderit in voluptate velit esse cillum dolore eu fugiat nulla pariatur. Excepteur sint occaecat cupidatat non proident, sunt in culpa qui officia deserunt mollit anim id est laborum.</p>
  <p class="tight">Lorem ipsum dolor sit amet, consectetur adipiscing elit, sed do eiusmod tempor incididunt ut labore et dolore magna aliqua. Ut enim ad minim veniam, quis nostrud exercitation ullamco laboris nisi ut aliquip ex ea commodo consequat. Duis aute irure dolor in reprehenderit in voluptate velit esse cillum dolore eu fugiat nulla pariatur. Excepteur sint occaecat cupidatat non proident, sunt in culpa qui officia deserunt mollit anim id est laborum.</p>
  <p>Lorem ipsum dolor sit amet, consectetur adipiscing elit, sed do eiusmod tempor incididunt ut labore et dolore magna aliqua. Ut enim ad minim veniam, quis nostrud exercitation ullamco laboris nisi ut aliquip ex ea commodo consequat. Duis aute irure dolor in reprehenderit in voluptate velit esse cillum dolore eu fugiat nulla pariatur. Excepteur sint.</p>
  <h2 class="h2">Heading</h2>
  <p>Standard Body Text - Lorem ipsum dolor sit amet, consectetur adipiscing elit, sed do eiusmod tempor incididunt ut labore et dolore magna aliqua. Ut enim ad minim veniam, quis nostrud exercitation ullamco laboris nisi ut aliquip ex ea commodo consequat. Duis aute irure dolor in reprehenderit in voluptate velit esse cillum dolore eu fugiat nulla pariatur. Excepteur sint occaecat cupidatat non proident, sunt in culpa qui officia deserunt mollit anim id est laborum.</p>
  <p>Lorem ipsum dolor sit amet, consectetur adipiscing elit, sed do eiusmod tempor incididunt ut labore et dolore magna aliqua. Ut enim ad minim veniam, quis nostrud exercitation ullamco laboris nisi ut aliquip ex ea commodo consequat. Duis aute irure dolor in reprehenderit in voluptate velit esse cillum dolore eu fugiat nulla pariatur. Excepteur sint occaecat cupidatat non proident, sunt in culpa qui officia deserunt mollit anim id est laborum.</p>
  <p>Standard Body Text - Lorem ipsum dolor sit amet, consectetur adipiscing elit, sed do eiusmod tempor incididunt ut labore et dolore magna aliqua. Ut enim ad minim veniam, quis nostrud exercitation ullamco laboris nisi ut aliquip ex ea commodo consequat. Duis aute irure dolor in reprehenderit in voluptate velit esse cillum dolore eu fugiat nulla pariatur. Excepteur sint occaecat cupidatat non proident, sunt in culpa qui officia deserunt mollit anim id est laborum.</p>
  <p class="tight">Lorem ipsum dolor sit amet, consectetur adipiscing elit, sed do eiusmod tempor incididunt ut labore et dolore magna aliqua. Ut enim ad minim veniam, quis nostrud exercitation ullamco laboris nisi ut aliquip ex ea commodo consequat. Duis aute irure dolor in reprehenderit in voluptate velit esse cillum dolore eu fugiat nulla pariatur. Excepteur sint occaecat cupidatat non proident, sunt in culpa qui officia deserunt mollit anim id est laborum.</p>
  <div class="photo building" role="img" aria-label="Modern office building with layered facade against a deep blue sky"></div>
  <p class="caption">Image Description / Credit</p>
  <p>Lorem ipsum dolor sit amet, consectetur adipiscing elit, sed do eiusmod tempor incididunt ut labore et dolore magna aliqua. Ut enim ad minim veniam, quis nostrud exercitation ullamco laboris nisi ut aliquip ex ea commodo consequat. Duis aute irure dolor in reprehenderit in voluptate velit esse cillum dolore eu fugiat nulla pariatur. Excepteur sint occaecat cupidatat non proident, sunt in culpa qui officia deserunt mollit anim id est laborum.</p>
</div>

<div class="col right">
  <h2 class="h2">Heading</h2>
  <p>Standard Body Text - Lorem ipsum dolor sit amet, consectetur adipiscing elit, sed do eiusmod tempor incididunt ut labore et dolore magna aliqua. Ut enim ad minim veniam, quis nostrud exercitation ullamco laboris nisi ut aliquip ex ea commodo consequat. Duis aute irure dolor in reprehenderit in voluptate velit esse cillum dolore eu fugiat nulla pariatur. Excepteur sint occaecat cupidatat non proident, sunt in culpa qui officia deserunt mollit anim id est laborum.</p>
  <p>Duis aute irure dolor in reprehenderit in voluptate velit esse cillum dolore eu fugiat nulla pariatur. Excepteur sint occaecat cupidatat non proident, sunt in culpa qui officia deserunt mollit anim id est laborum.</p>
  <div class="photo glass" role="img" aria-label="Glass atrium with stairs and planting overlooking city rooftops"></div>
  <p class="caption">Image Description / Credit</p>
  <p>Standard Body Text - Lorem ipsum dolor sit amet, consectetur adipiscing elit, sed do eiusmod tempor incididunt ut labore et dolore magna aliqua. Ut enim ad minim veniam, quis nostrud exercitation ullamco laboris nisi ut aliquip ex ea commodo consequat. Duis aute irure dolor in reprehenderit in voluptate velit esse cillum dolore eu fugiat nulla pariatur. Excepteur sint occaecat cupidatat non proident, sunt in culpa qui officia deserunt mollit anim id est laborum.</p>
  <p>Lorem ipsum dolor sit amet, consectetur adipiscing elit, sed do eiusmod tempor incididunt ut labore et dolore magna aliqua. Ut enim ad minim veniam, quis nostrud exercitation ullamco laboris nisi ut aliquip ex ea commodo consequat. Duis aute irure dolor in reprehenderit in voluptate velit esse cillum dolore eu fugiat nulla pariatur. Excepteur sint occaecat cupidatat non proident, sunt in culpa qui officia deserunt mollit anim id est laborum.</p>
  <p>Standard Body Text - Lorem ipsum dolor sit amet, consectetur adipiscing elit, sed do eiusmod tempor incididunt ut labore et dolore magna aliqua. Ut enim ad minim veniam, quis nostrud exercitation ullamco laboris nisi ut aliquip ex ea commodo consequat. Duis aute irure dolor in reprehenderit in voluptate velit esse cillum dolore eu fugiat nulla pariatur. Excepteur sint occaecat cupidatat non proident, sunt in culpa qui officia deserunt mollit anim id est laborum.</p>
  <p>Lorem ipsum dolor sit amet, consectetur adipiscing elit, sed do eiusmod tempor incididunt ut labore et dolore magna aliqua. Ut enim ad minim veniam, quis nostrud exercitation ullamco laboris nisi ut aliquip ex ea commodo consequat. Duis aute irure dolor in reprehenderit in voluptate velit esse cillum dolore eu fugiat nulla pariatur. Excepteur sint occaecat cupidatat non proident, sunt in culpa qui officia deserunt mollit anim id est laborum.</p>
</div>

<a class="to-top" aria-label="Back to top">
  <svg width="54" height="54" viewBox="0 0 54 54"><polyline points="20,30 27,23 34,30" fill="none" stroke="#2b2b2b" stroke-width="2"/></svg>
</a>

<footer class="site-footer">
  <nav class="footer-nav"><span>About</span><span>Contact</span><span>Property</span><span>Capital &amp; Finance</span></nav>
  <div class="social" aria-label="Social links"><i></i><i></i><i></i></div>
</footer>

<div class="base-bar">
  <span class="copy">© Copyright 2018 - 2019 &nbsp;| &nbsp; All Rights Reserved</span>
  <span class="contact">
    <svg width="9" height="9" viewBox="0 0 24 24" style="vertical-align:-1px;margin-right:4px"><path fill="#fff" d="M6.6 10.8a15 15 0 0 0 6.6 6.6l2.2-2.2c.3-.3.7-.4 1-.2 1.1.4 2.3.6 3.6.6.6 0 1 .4 1 1V20c0 .6-.4 1-1 1A17 17 0 0 1 3 4c0-.6.4-1 1-1h3.5c.6 0 1 .4 1 1 0 1.3.2 2.5.6 3.6.1.3 0 .7-.2 1z"/></svg>(02) 9000 4172 &nbsp;| &nbsp;CONTACT / MEDIA INQUIRIES
  </span>
</div>
</body>
</html>
```